Harbor Business Cards

I need a business card designed with the following information.

Company Name: Harbor Wealth Management
Name: BriAnne Dockery
Title: Executive Assistant
Cell: (281) 555-0173
Direct Line: (832) 555-0148
Email: brianne@harborwmx.com
Address: 20537 W. Marlowe PKWY Ste. B
Tomball, TX 77390

I have attached the logo.
I would like it in navy blue and silver.
Thanks.

```html
<!DOCTYPE html>
<html lang="en">
<head>
<meta charset="utf-8">
<title>Harbor Wealth Management – Business Card</title>
<link rel="stylesheet" href="https://fonts.googleapis.com/css2?family=Tenor+Sans&display=swap">
<style>
  :root {
    --navy: #1c2640;
    --silver: #c8c7c9;
    --paper: #ffffff;
    --edge: #bdbdbd;
    --ink: #1c2640;
  }
  html, body {
    margin: 0;
    padding: 0;
    width: 1200px;
    height: 1159px;
    overflow: hidden;
    background: var(--paper);
  }
  .sheet {
    position: relative;
    width: 1200px;
    height: 1159px;
    font-family: "Tenor Sans", sans-serif;
  }
  .card-front {
    position: absolute;
    left: 306px;
    top: 110px;
    width: 627px;
    height: 390px;
    background: var(--navy);
    overflow: hidden;
  }
  .card-front .corner {
    position: absolute;
    left: 0;
    top: 0;
  }
  .brand {
    position: absolute;
    left: 30px;
    top: 210px;
    width: 430px;
    text-align: center;
    color: var(--paper);
  }
  .brand-name {
    font-size: 38px;
    letter-spacing: 15px;
    line-height: 1;
    margin: 0 0 0 15px;
  }
  .brand-sub {
    font-size: 13px;
    letter-spacing: 3.4px;
    margin-top: 18px;
  }
  .card-back {
    position: absolute;
    left: 311px;
    top: 647px;
    width: 620px;
    height: 386px;
    border: 1px solid var(--edge);
    background: var(--paper);
    color: var(--ink);
  }
  .contact {
    position: absolute;
    left: 74px;
    top: 55px;
    font-size: 20px;
    line-height: 26px;
  }
  .contact p { margin: 0; }
  .contact .name { font-size: 22px; letter-spacing: 0.5px; }
  .contact .gap { margin-top: 26px; }
</style>
</head>
<body>
<main class="sheet">
  <section class="card-front" aria-label="Card front">
    <svg class="corner" width="627" height="390" viewBox="0 0 627 390" aria-hidden="true">
      <polygon points="339,0 627,0 627,335" fill="var(--silver)"/>
    </svg>
    <div class="brand">
      <p class="brand-name">HARBOR</p>
      <div class="brand-sub">WEALTH MANAGEMENT</div>
    </div>
  </section>

  <section class="card-back" aria-label="Card back">
    <div class="contact">
      <p class="name">BRIANNE DOCKERY</p>
      <p>Executive Assistant</p>
      <p class="gap">Cell: (281) 555-0173</p>
      <p>Direct Line: (832) 555-0148</p>
      <p class="gap">brianne@harborwmx.com</p>
      <p class="gap">20537 W. Marlowe PKWY Ste. B</p>
      <p>Tomball, TX 77390</p>
    </div>
  </section>
</main>
</body>
</html>
```